The Quiet Lantern - The best guide in your pocket

The Quiet Lantern (فانوس‌آرام in Persian)

We need a new app design for a major update on Android, iOS and Windows Universal platforms.
Our company works on creating innovative apps and games on different platforms, this particular app is free for end users and provides location based services. Here is the abstract feature list:
• Nearest points around user (explore on map or find) including locations, events and skills
• Add points to our database (partners) plus comments and ratings
• Point owners can modify or complete their points data, provide sale events, services and …

Attachments:
Our service logo
The detailed descriptions of different sections (PDF documents)
Updates

Project Deadline Extended Reason: We want more designs :)Give us previews on Home and Map sections at least (more interesting if previews are provided for more sections) Added Saturday, January 7, 2017

Target Market(s)

Public

Industry/Entity Type

Android

Font styles to use
Serif
Sans Serif

Requirements
Must have
• Consider attached service logo & wireframe
• Designs for attached sections
• Fluent user experience
• Modern design
Nice to have
• Right to Left layouts
Should not have
• No alphabet in graphic assets

```html
<!DOCTYPE html>
<html lang="en">
<head>
<meta charset="utf-8">
<title>The Quiet Lantern – Sign in</title>
<link rel="stylesheet" href="https://fonts.googleapis.com/css2?family=Roboto:wght@300;400;500&family=Vazirmatn:wght@700&display=swap">
<style>
  :root {
    --slate: #46637a;
    --slate-dark: #3c5566;
    --ink: #3f5f6e;
    --muted: #7a8a92;
    --white: #ffffff;
    --sky-top: #ffffff;
    --sky-mid: #e3edf3;
    --crowd: #c6c8cb;
  }
  * { box-sizing: border-box; margin: 0; padding: 0; }
  html, body { width: 674px; height: 1200px; overflow: hidden; }
  body { font-family: "Roboto", "Vazirmatn", sans-serif; background: var(--white); position: relative; }

  .backdrop {
    position: absolute; inset: 0;
    background:
      radial-gradient(ellipse 60% 40% at 50% 62%, rgba(170,175,182,0.55), rgba(170,175,182,0) 70%),
      linear-gradient(180deg, var(--sky-top) 0%, #f4f8fb 18%, var(--sky-mid) 45%, #d9dde1 70%, var(--crowd) 100%);
  }

  .status-bar {
    position: absolute; top: 0; left: 0; right: 0; height: 44px;
    display: flex; align-items: center; justify-content: space-between;
    padding: 0 12px 0 12px;
    color: var(--slate); font-weight: 300; font-size: 23px;
  }
  .status-bar .carrier { display: flex; align-items: center; gap: 8px; }
  .status-bar .time { position: absolute; left: 0; right: 0; text-align: center; pointer-events: none; }
  .status-bar .right { display: flex; align-items: center; gap: 10px; }

  .brand {
    position: absolute; top: 118px; left: 0; right: 0;
    text-align: center; direction: rtl;
    font-family: "Roboto", "Vazirmatn", sans-serif;
    font-weight: 700; font-size: 62px; color: var(--ink);
  }

  .form { position: absolute; left: 48px; width: 578px; top: 816px; }
  .field {
    display: flex; height: 82px; background: var(--white);
    box-shadow: 0 2px 2px rgba(0,0,0,0.25);
  }
  .field .icon {
    width: 83px; background: var(--slate);
    display: flex; align-items: center; justify-content: center;
  }
  .field .input {
    flex: 1; display: flex; align-items: center; justify-content: center;
    font-size: 21px; color: var(--muted); padding-right: 20px;
  }
  .btn {
    display: flex; align-items: center; justify-content: center;
    height: 83px; font-size: 21px;
  }
  .btn-outline {
    margin-top: 32px; border: 1px solid var(--slate-dark); color: var(--slate);
    box-shadow: 0 2px 2px rgba(0,0,0,0.3);
  }
  .btn-primary {
    margin-top: 31px; background: var(--slate); color: var(--white);
    font-size: 18px; font-weight: 500; box-shadow: 0 2px 2px rgba(0,0,0,0.25);
  }
</style>
</head>
<body>
  <div class="backdrop" role="img" aria-label="Faded photo of a concert crowd with raised hands against a bright sky"></div>

  <div class="status-bar">
    <div class="carrier">
      <svg width="74" height="14" viewBox="0 0 74 14" aria-hidden="true">
        <g fill="#46637a"><circle cx="7" cy="7" r="6"/><circle cx="22" cy="7" r="6"/><circle cx="37" cy="7" r="6"/></g>
        <g fill="none" stroke="#46637a" stroke-width="1.4"><circle cx="52" cy="7" r="5.3"/><circle cx="67" cy="7" r="5.3"/></g>
      </svg>
      <span>LUMA</span>
      <svg width="26" height="20" viewBox="0 0 26 20" aria-hidden="true">
        <path d="M13 18 L17 13.5 A6 6 0 0 0 9 13.5 Z" fill="#46637a"/>
        <path d="M5.5 10 A10.5 10.5 0 0 1 20.5 10" fill="none" stroke="#46637a" stroke-width="2.6"/>
        <path d="M1.5 6 A16 16 0 0 1 24.5 6" fill="none" stroke="#46637a" stroke-width="2.6"/>
      </svg>
    </div>
    <div class="time">4:21 PM</div>
    <div class="right">
      <svg width="14" height="24" viewBox="0 0 14 24" aria-hidden="true">
        <path d="M2 7 L12 17 L7 22 V2 L12 7 L2 17" fill="none" stroke="#9aa6ad" stroke-width="1.5"/>
      </svg>
      <span>100%</span>
      <svg width="52" height="22" viewBox="0 0 52 22" aria-hidden="true">
        <rect x="1" y="2" width="46" height="18" rx="3" fill="none" stroke="#46637a" stroke-width="1.5"/>
        <rect x="3.5" y="4.5" width="41" height="13" rx="1.5" fill="#46637a"/>
        <rect x="48.5" y="8" width="2.5" height="6" rx="1" fill="#46637a"/>
      </svg>
    </div>
  </div>

  <div class="brand">فانوس‌آرام</div>

  <div class="form">
    <div class="field">
      <div class="icon">
        <svg width="28" height="46" viewBox="0 0 28 46" aria-hidden="true">
          <rect x="2" y="1.5" width="24" height="43" rx="4" fill="none" stroke="#fff" stroke-width="3"/>
          <rect x="5.5" y="8" width="17" height="26" fill="#fff"/>
          <circle cx="14" cy="39" r="2" fill="#fff"/>
          <rect x="10" y="4.5" width="8" height="1.5" fill="#fff"/>
        </svg>
      </div>
      <div class="input">Enter the phone number</div>
    </div>
    <div class="btn btn-outline">Verification Code Recieved</div>
    <div class="btn btn-primary">RETRY</div>
  </div>
</body>
</html>
```